Exciting, Bold and Modern Landscaping & Turf care company business card

Hello, I own a lawn and landscaping company in Virginia, USA. We would like to design a bold, dynamic, modern business card that really makes us stand out. I tire of all green business cards with crappy, cartoonish clipart grass on them. It needs to be two sided, on one side i need to highlight our turf care division called "Certified Lusher Lawns" We maintain grass, fertilize it, weed control, etc.. We have a green thumbed gopher as our logo that i will attach. I am looking for something, clean and neat but out of the box in style. Im open to all ideas, and would like different options for them. On the other side, i want to highlight our landscaping division "Willow Bend Landscaping" In this division we design and install landscapes. Feel free to visit our website for more info or email me with ANY questions. Our busines cards in the past have highlighted our different services, but i don't want to this time. By the time I hand out a business card we are usually already estimating a project and they know what services we offer. I do want them to look at my card and say "wow thats pretty cool" and for them to think "These guys are something different, not just your standard dirt diggers" The logo doesnt have to be on both sides, but it needs to be on the turf care side. Our phone number and website should also be on at least on side, but need not be on both. The phone number is (555)218-6047 as well as the web address as www.OurGardenCrewExample.com. I like for the web address to have caps like that becasue it makes the long address much easier to read. I would like it in full color, printing costs are not my major concern. I also love rounded corners or interesting die cut designs as well, so feel free to wow me. Whether it be a clean white background with a bold photo to an all black card with a gray logo except for his green thumb with silver foil lettering to anything in between, lets go for it. That bieng said i dont want anything cartoonish, we are still a professional service and i want that to come through. THANKS!
Reason: changed project to a committed payment. I would like designers to re-evaluate their interest now and give them extra time to submit designs. Thank you.
we have changed our status to a commited payment to entice more submissions. thank you all for your hard work!

```html
<!DOCTYPE html>
<html lang="en">
<head>
<meta charset="utf-8">
<title>Willow Bend Landscaping – Business Card</title>
<link rel="stylesheet" href="https://fonts.googleapis.com/css2?family=Open+Sans:wght@600;700&family=Arimo:ital,wght@1,400;1,700&display=swap">
<style>
  :root {
    --page-bg: #ece7e1;
    --turf-dark: #1f6b2a;
    --turf-mid: #2f8a3a;
    --turf-light: #4aa84f;
    --brand-green: #0b7a3e;
    --accent-orange: #e0782a;
    --mascot-tan: #d9863f;
    --ink: #111111;
    --paper: #ffffff;
  }
  * { box-sizing: border-box; margin: 0; padding: 0; }
  html, body { width: 1200px; height: 988px; overflow: hidden; }
  body {
    background: var(--page-bg);
    position: relative;
    font-family: "Arimo", Arial, sans-serif;
  }
  .card {
    position: absolute;
    left: 250px;
    width: 700px;
    height: 400px;
    border-radius: 28px;
    overflow: hidden;
    box-shadow: 0 6px 18px rgba(0,0,0,0.18);
  }

  /* Turf side */
  .card--turf {
    top: 64px;
    background: radial-gradient(ellipse at 30% 75%, var(--turf-light) 0%, var(--turf-mid) 45%, var(--turf-dark) 100%);
  }
  .card--turf .mascot {
    position: absolute;
    left: 140px;
    top: 170px;
    width: 250px;
    height: 230px;
    border-radius: 46% 46% 0 0;
    background: linear-gradient(180deg, var(--mascot-tan) 0%, #b8642a 100%);
  }
  .card--turf .tagline {
    position: absolute;
    right: 40px;
    bottom: 48px;
    width: 300px;
    font-family: "Open Sans", Arial, sans-serif;
    font-weight: 700;
    font-size: 22px;
    line-height: 1.2;
    color: var(--paper);
    text-align: right;
  }

  /* Contact side */
  .card--contact {
    top: 524px;
    background: var(--paper);
  }
  .card--contact .wave {
    position: absolute;
    inset: 0;
    width: 700px;
    height: 400px;
  }
  .person {
    position: absolute;
    left: 56px;
    top: 34px;
  }
  .person__name {
    font-family: "Open Sans", Arial, sans-serif;
    font-weight: 700;
    font-size: 26px;
    line-height: 1.2;
    color: var(--brand-green);
    letter-spacing: 0.5px;
  }
  .person__role {
    font-style: italic;
    font-size: 15px;
    color: var(--ink);
    margin-top: 2px;
  }
  .contact-list {
    position: absolute;
    left: 56px;
    top: 108px;
    list-style: none;
  }
  .contact-list li {
    display: flex;
    align-items: center;
    gap: 12px;
    font-style: italic;
    font-size: 20px;
    line-height: 24px;
    color: var(--ink);
    height: 24px;
  }
  .contact-list svg { width: 18px; height: 18px; flex: none; }
  .card--contact .mascot {
    position: absolute;
    left: 470px;
    top: 56px;
    width: 190px;
    height: 190px;
    border-radius: 46% 46% 10px 10px;
    background: linear-gradient(180deg, var(--mascot-tan) 0%, #c06e30 100%);
  }
  .card--contact .tagline {
    position: absolute;
    left: 36px;
    top: 262px;
    font-style: italic;
    font-size: 26px;
    line-height: 1.15;
    color: var(--paper);
  }
</style>
</head>
<body>

  <section class="card card--turf">
    <div class="mascot" role="img" aria-label="Gopher mascot giving a thumbs-up with a green thumb"></div>
    <p class="tagline">Willow Bend Landscaping and Certified Lusher Lawns</p>
  </section>

  <section class="card card--contact">
    <svg class="wave" viewBox="0 0 700 400" aria-hidden="true">
      <path d="M0 190 C 260 192, 460 272, 700 300 L700 309 C 460 281, 260 201, 0 199 Z" fill="var(--accent-orange)"/>
      <path d="M450 250 C 550 270, 630 280, 700 276 L700 286 C 630 292, 550 282, 450 250 Z" fill="var(--brand-green)"/>
      <path d="M0 208 C 260 210, 460 290, 700 322 L700 400 L0 400 Z" fill="var(--brand-green)"/>
    </svg>

    <div class="person">
      <h1 class="person__name">Marco Ellison</h1>
      <p class="person__role">General Manager</p>
    </div>

    <ul class="contact-list">
      <li>
        <svg viewBox="0 0 20 20"><path d="M3 8 C3 4 17 4 17 8 L14 9 L13 7 C11 6.5 9 6.5 7 7 L6 9 Z M5 10 H15 L16 16 H4 Z" fill="var(--brand-green)"/></svg>
        (555)218-6047
      </li>
      <li>
        <svg viewBox="0 0 20 20"><path d="M2 9 L10 3 L18 9 V17 H2 Z" fill="none" stroke="var(--brand-green)" stroke-width="2"/><path d="M2 9 L10 14 L18 9" fill="none" stroke="var(--brand-green)" stroke-width="2"/></svg>
        info@OurGardenCrewExample.com
      </li>
      <li>
        <svg viewBox="0 0 20 20"><circle cx="10" cy="10" r="8" fill="none" stroke="var(--brand-green)" stroke-width="2"/><path d="M2 10 H18 M10 2 C6 6 6 14 10 18 M10 2 C14 6 14 14 10 18" fill="none" stroke="var(--brand-green)" stroke-width="1.5"/></svg>
        www.OurGardenCrewExample.com
      </li>
    </ul>

    <div class="mascot" role="img" aria-label="Gopher mascot on a tuft of grass giving a thumbs-up with a green thumb"></div>

    <p class="tagline">Willow Bend Landscaping<br>and Certified Lusher Lawns</p>
  </section>

</body>
</html>
```